Business Card Design for Technology Company

New business card design needed for technology company director.
Ideally, the design will fit the style and nature of the industry. We are a supplier of quality products and services, and we hope the design will give customers and suppliers this impression.

Target Market(s)

3D Printing Industry

Industry/Entity Type

Technology Equipment

Contact Information for Business Card

Name: Marcus Lyle
Title: Director
Company address: Factory K4, 7B Morland Road, Kelbrook Westmere Australia 3472
Telephone: +61-3-8555 6413
Email: marcus.lyle@veranox.com.au
Website: www.veranox.com.au

Requirements
Must have
• All information in business card details
• Company logo
• '3D Printers and 3D Print Filaments' at proper place
Nice to have
• Style to fit the industry
• Colour to fit logo

```html
<!DOCTYPE html>
<html lang="en">
<head>
<meta charset="utf-8">
<title>Veranox Technology – Business Card</title>
<link rel="stylesheet" href="https://fonts.googleapis.com/css2?family=Josefin+Sans:wght@100;200;300;400;600&display=swap">
<style>
  :root {
    --steel-blue: #6a97b8;
    --ink: #161616;
    --card: #ffffff;
    --bg-light: #d9d9d9;
    --bg-dark: #6c6b6b;
    --font: "Josefin Sans", sans-serif;
  }
  * { box-sizing: border-box; margin: 0; padding: 0; }
  html, body { width: 1200px; height: 1200px; overflow: hidden; }
  body {
    background: radial-gradient(circle at 50% 50%, var(--bg-light) 0%, #a9a8a8 55%, var(--bg-dark) 100%);
    font-family: var(--font);
    color: var(--ink);
    position: relative;
  }
  .card {
    position: absolute;
    left: 322px;
    width: 557px;
    height: 328px;
    background: var(--card);
    overflow: hidden;
  }
  .card--front { top: 249px; }
  .card--back { top: 623px; }
  .card__pattern { position: absolute; inset: 0; width: 100%; height: 100%; }
  .card__pattern path { fill: var(--steel-blue); }

  .brand { position: absolute; color: var(--ink); font-weight: 600; text-transform: uppercase; line-height: 1; }
  .brand__mark { display: block; flex: none; background: var(--steel-blue); }
  .brand__name { display: block; }
  .brand__sub { display: block; }

  .card--front .brand { left: 280px; top: 78px; width: 176px; text-align: center; }
  .card--front .brand__mark { width: 80px; height: 80px; margin: 0 auto 46px; }
  .card--front .brand__name { font-size: 31px; letter-spacing: 6px; margin-left: 6px; }
  .card--front .brand__sub { font-size: 10px; letter-spacing: 7.4px; margin-top: 6px; margin-left: 7px; }

  .card--back .brand { left: 324px; top: 38px; display: flex; align-items: center; gap: 14px; }
  .card--back .brand__mark { width: 48px; height: 48px; }
  .card--back .brand__name { font-size: 23px; letter-spacing: 4.5px; }
  .card--back .brand__sub { font-size: 8px; letter-spacing: 5.4px; margin-top: 4px; }

  .person__title { position: absolute; left: 56px; top: 66px; font-size: 16px; font-weight: 400; }
  .person__name { position: absolute; left: 73px; top: 84px; font-size: 38px; font-weight: 200; letter-spacing: 0.5px; color: var(--ink); }

  .contact { list-style: none; }
  .contact__item { position: absolute; left: 33px; display: flex; align-items: center; font-size: 17.5px; font-weight: 400; white-space: nowrap; }
  .contact__icon { width: 24px; height: 24px; flex: none; margin-right: 18px; }
  .contact__icon circle { fill: var(--steel-blue); }
  .contact__icon .glyph { fill: #fff; stroke: none; }
  .contact__icon .line { fill: none; stroke: #fff; stroke-width: 1.3; }
  .contact__item--phone { top: 148px; }
  .contact__item--web { top: 182px; }
  .contact__item--mail { top: 218px; }
  .contact__item--address { top: 253px; align-items: flex-start; }
  .address { line-height: 20px; }
  .address span { display: block; text-align: right; }
</style>
</head>
<body>

<section class="card card--front" aria-label="Business card front">
  <svg class="card__pattern" viewBox="0 0 697 410" preserveAspectRatio="none" aria-hidden="true">
    <path d="M0 0 L78 0 L130 92 L0 274 Z"/>
    <path d="M118 0 L275 0 L331 87 L166 410 L0 410 L0 321 L170 92 Z"/>
  </svg>
  <div class="brand">
    <span class="brand__mark" aria-hidden="true"></span>
    <span class="brand__name">Veranox</span>
    <span class="brand__sub">Technology</span>
  </div>
</section>

<section class="card card--back" aria-label="Business card back">
  <svg class="card__pattern" viewBox="0 0 697 410" preserveAspectRatio="none" aria-hidden="true">
    <path d="M423 0 L578 0 L526 92 L697 322 L697 410 L531 410 L365 87 Z"/>
    <path d="M619 0 L697 0 L697 274 L567 92 Z"/>
  </svg>

  <div class="brand">
    <span class="brand__mark" aria-hidden="true"></span>
    <div>
      <span class="brand__name">Veranox</span>
      <span class="brand__sub">Technology</span>
    </div>
  </div>

  <p class="person__title">Director</p>
  <h1 class="person__name">Marcus Lyle</h1>

  <ul class="contact">
    <li class="contact__item contact__item--phone">
      <svg class="contact__icon" viewBox="0 0 24 24" aria-hidden="true">
        <circle cx="12" cy="12" r="12"/>
        <path class="glyph" d="M8.2 6.2c.5-.4 1.1-.3 1.4.2l1.2 2c.3.5.2 1-.2 1.3l-.8.6c.6 1.4 1.7 2.6 3.1 3.3l.7-.8c.4-.4.9-.5 1.3-.2l2 1.2c.5.3.6 1 .2 1.4l-1 1.1c-.6.6-1.5.8-2.3.5-3.2-1.2-5.6-3.7-6.7-6.9-.3-.8 0-1.7.6-2.2z"/>
      </svg>
      <span>+61-3-8555 6413</span>
    </li>
    <li class="contact__item contact__item--web">
      <svg class="contact__icon" viewBox="0 0 24 24" aria-hidden="true">
        <circle cx="12" cy="12" r="12"/>
        <circle class="line" cx="12" cy="12" r="7" style="fill:none"/>
        <ellipse class="line" cx="12" cy="12" rx="3" ry="7"/>
        <path class="line" d="M5 12h14M6.5 8.5h11M6.5 15.5h11"/>
      </svg>
      <span>www.veranox.com.au</span>
    </li>
    <li class="contact__item contact__item--mail">
      <svg class="contact__icon" viewBox="0 0 24 24" aria-hidden="true">
        <circle cx="12" cy="12" r="12"/>
        <rect class="line" x="6.5" y="8" width="11" height="8" rx="0.8"/>
        <path class="line" d="M6.8 8.4 12 12.6l5.2-4.2M6.8 15.6l3.8-3.8M17.2 15.6l-3.8-3.8"/>
      </svg>
      <span>marcus.lyle@veranox.com.au</span>
    </li>
    <li class="contact__item contact__item--address">
      <svg class="contact__icon" viewBox="0 0 24 24" aria-hidden="true">
        <circle cx="12" cy="12" r="12"/>
        <path class="glyph" d="M12 5.5a4.5 4.5 0 0 0-4.5 4.5c0 3.3 4.5 8.5 4.5 8.5s4.5-5.2 4.5-8.5A4.5 4.5 0 0 0 12 5.5zm0 6.3a1.8 1.8 0 1 1 0-3.6 1.8 1.8 0 0 1 0 3.6z"/>
      </svg>
      <span class="address">
        <span>Factory K4, 7B Morland Road, Kelbrook Westmere</span>
        <span>Australia 3472</span>
      </span>
    </li>
  </ul>
</section>

</body>
</html>
```